(Expedite)Stationary/Business card design for Accounting Firm
Lumen CPA Partners
(Expedite)Stationary/Business card design for Accounting Firm - Financial Services
Creative Brief
Professional
Given R. Surname, CPA
58 North Birch Avenue, 6th Floor Waterbury, CT 06419
employee@lumencpa.net
www.lumencpa.net
We would like a nice modern, clean look that's fitting for a professional accounting firm image. We'd like to stick with colors matching the logo. Please use sample information for design purposes. Mainly, we're in need of: - Business card - Letterhead - Envelope - Presentation (tax) folder - E-mail signature - Invoice form (will need Word-based format) - Fax cover (Word-based) - Notepad (8.5 x 5.5) Use icons to indicate phone, fax, mobile, etc. Good luck!
Logo symbol and website address

```html
<!DOCTYPE html>
<html lang="en">
<head>
<meta charset="utf-8">
<title>Lumen CPA Partners – Stationery Set</title>
<link rel="stylesheet" href="https://fonts.googleapis.com/css2?family=Montserrat:wght@600&family=Open+Sans:wght@400;600&display=swap">
<style>
  :root{
    --bg:#2b1d15;
    --navy:#1d2670;
    --blue:#2c3aa0;
    --paper:#ffffff;
    --ink:#3a3a48;
    --rule:#c9ccd8;
    --muted:#8a8ea3;
  }
  *{box-sizing:border-box;margin:0;padding:0}
  html,body{width:1200px;height:192px;overflow:hidden;background:var(--bg)}
  body{position:relative;font-family:"Open Sans",sans-serif;color:var(--ink)}
  .piece{position:absolute;background:var(--paper);box-shadow:0 1px 3px rgba(0,0,0,.5);overflow:hidden}
  .brand{display:flex;align-items:center;gap:3px;font-family:"Montserrat",sans-serif;font-weight:600;color:var(--navy);white-space:nowrap}
  .brand .mark{width:7px;height:7px;background:var(--navy);flex:none}
  .brand.light{color:var(--paper)}
  .brand.light .mark{background:var(--paper)}
  .tiny{font-size:4px;line-height:5.5px}
  .micro{font-size:3px;line-height:4px;white-space:nowrap}
  .bar{height:2px;background:var(--rule);margin:2px 0}
  .footer-band{position:absolute;left:0;right:0;bottom:0;height:7px;background:var(--navy)}
  .page{top:20px;width:118px;height:152px;padding:8px}
  .page .brand{font-size:6px}
  .page .body{margin-top:14px}
  .page h4{font-family:"Montserrat",sans-serif;font-size:7px;color:var(--navy);margin:10px 0 4px}
  .table-row{display:flex;justify-content:space-between;border-bottom:1px solid var(--rule);padding:1px 0}
  .card{width:66px;height:38px;padding:4px}
  .card.dark{background:var(--navy)}
  .card .brand{font-size:4px;gap:2px}
  .card .brand .mark{width:5px;height:5px}
  .folder{top:14px;height:164px;background:var(--navy)}
  .folder .cap{position:absolute;left:0;right:0;top:0;height:52px;background:var(--paper)}
  .curve{position:absolute;left:0;width:100%}
</style>
</head>
<body>

<!-- Business cards -->
<div class="piece card" style="left:8px;top:52px">
  <div class="brand"><span class="mark"></span>Lumen CPA Partners</div>
  <p class="micro" style="margin-top:5px">Given R. Surname, CPA<br>employee@lumencpa.net<br>www.lumencpa.net</p>
</div>
<div class="piece card dark" style="left:8px;top:96px">
  <div class="brand light" style="margin-top:10px"><span class="mark"></span>Lumen CPA Partners</div>
  <p class="micro" style="color:#cfd3f0;margin-top:3px">Certified Public Accountants</p>
</div>

<!-- Letterhead -->
<div class="piece page" style="left:96px">
  <div class="brand"><span class="mark"></span>Lumen CPA Partners</div>
  <div class="body tiny">
    <p>Dear Client,</p>
    <p style="margin-top:3px">Thank you for your trust in our firm.</p>
    <div class="bar"></div><div class="bar"></div><div class="bar" style="width:80%"></div>
    <p>We look forward to serving you.</p>
    <div class="bar"></div><div class="bar" style="width:60%"></div>
    <p style="margin-top:6px">Sincerely,</p>
    <p>Given R. Surname, CPA</p>
  </div>
  <p class="micro" style="position:absolute;bottom:10px;left:8px;right:8px;white-space:normal">58 North Birch Avenue, 6th Floor Waterbury, CT 06419 · www.lumencpa.net</p>
  <div class="footer-band"></div>
</div>

<!-- Invoice -->
<div class="piece page" style="left:226px">
  <div class="brand"><span class="mark"></span>Lumen CPA Partners</div>
  <h4>INVOICE</h4>
  <div class="tiny">
    <div class="table-row" style="background:var(--navy);color:#fff;padding:1px 2px"><span>Description</span><span>Amount</span></div>
    <div class="table-row">&nbsp;</div><div class="table-row">&nbsp;</div><div class="table-row">&nbsp;</div>
    <div class="table-row">&nbsp;</div><div class="table-row">&nbsp;</div>
    <div class="table-row" style="justify-content:flex-end;font-weight:600"><span>Total</span></div>
  </div>
  <div class="footer-band"></div>
</div>

<!-- Fax cover -->
<div class="piece page" style="left:356px">
  <div class="brand"><span class="mark"></span>Lumen CPA Partners</div>
  <h4>FAX</h4>
  <div class="tiny">
    <p>To:</p><div class="bar"></div>
    <p>From:</p><div class="bar"></div>
    <p>Pages:</p><div class="bar"></div>
  </div>
  <div class="footer-band"></div>
</div>

<!-- Notepad -->
<div class="piece page" style="left:486px">
  <div class="brand"><span class="mark"></span>Lumen CPA Partners</div>
  <h4>Notes</h4>
  <div class="bar"></div><div class="bar"></div><div class="bar"></div><div class="bar"></div>
  <div class="bar"></div><div class="bar"></div><div class="bar"></div><div class="bar"></div>
  <div class="footer-band"></div>
</div>

<!-- Envelope -->
<div class="piece" style="left:620px;top:70px;width:120px;height:54px;padding:5px">
  <div class="brand" style="font-size:5px"><span class="mark"></span>Lumen CPA Partners</div>
  <p class="micro">58 North Birch Avenue, 6th Floor<br>Waterbury, CT 06419</p>
  <div class="footer-band" style="height:5px"></div>
</div>

<!-- E-mail signature card -->
<div class="piece card" style="left:750px;top:78px">
  <p class="micro" style="font-weight:600">Given R. Surname, CPA</p>
  <div class="brand" style="margin-top:3px"><span class="mark"></span>Lumen CPA Partners</div>
  <p class="micro" style="margin-top:2px">employee@lumencpa.net</p>
</div>

<!-- Folder, closed -->
<div class="piece folder" style="left:830px;width:120px">
  <div class="cap"></div>
  <svg class="curve" style="top:40px" width="120" height="24" viewBox="0 0 120 24"><path d="M0 12 Q60 -4 120 12 V24 H0Z" fill="#1d2670"/></svg>
  <div class="brand light" style="position:absolute;left:18px;top:90px;font-size:8px"><span class="mark" style="width:9px;height:9px"></span>Lumen CPA Partners</div>
</div>

<!-- Folder, open -->
<div class="piece folder" style="left:960px;width:230px;background:var(--paper)">
  <div style="position:absolute;left:0;top:0;width:115px;height:100%;background:#f1f2f7"></div>
  <div style="position:absolute;left:114px;top:0;width:1px;height:100%;background:var(--rule)"></div>
  <svg class="curve" style="bottom:0" width="230" height="64" viewBox="0 0 230 64"><path d="M0 10 Q57 0 115 10 V64 H0Z M115 10 Q172 0 230 10 V64 H115Z" fill="#2c3aa0"/></svg>
  <div class="piece card" style="left:140px;top:112px;width:50px;height:28px;padding:3px">
    <div class="brand" style="font-size:3px"><span class="mark" style="width:4px;height:4px"></span>Lumen CPA Partners</div>
  </div>
</div>

</body>
</html>
```